Book Cover for Horror Novel - HOLLOWED

I need a book cover for a horror novel called HOLLOWED.
The setting is an old house full of portraits. A team has been dispatched to catalogue the art and antiques. Every wall is covered with portraits - oil paintings, watercolours, sketches. The art terrorises the team from the auction house. Think "Trevisanolo Meets Gravemarch".
I'm looking for a cover which leans more towards the art side of the story. I like the idea of using a famous artist's self portrait, but smearing the face or something similar. Or a wall full of portraits.
I have a Corkwall board where I've posted a number of images I've used as inspiration in the novel which may be of assistance: https://nz.corkwall.com/rimuwriter/hollowed-a-novel/

Title: Hollowed
Author: Marlene Osgood
Tagline: Why, in a house full of portraits, does one stand unfinished?

Target Market(s)

Adults - men and women. Readers of Dorian Welt type horror novels

Industry/Entity Type

House

Other font styles liked:
• Hoefler Text

Requirements
Must have
• Book Title: Hollowed
• Author Name: Marlene Osgood
• Tag Line: Why, in a house full of portraits, does one stand unfinished?
• Image or images of portraits - preferably oil paintings, because the brush strokes of an oil painting are so vivid compared to watercolours.
Nice to have
• Lots of portraits, but I am comfortable with one striking image.
• Other imagery in the book - ravens / a child / a collection of netsuke - including a jade dog - images of these are on my corkwall page in this link https://nz.corkwall.com/rimuwriter/hollowed-a-novel/
• I like the font Hoefler Text, but I am open to others.

```html
<!DOCTYPE html>
<html lang="en">
<head>
<meta charset="utf-8">
<title>Hollowed — Marlene Osgood</title>
<link rel="stylesheet" href="https://fonts.googleapis.com/css2?family=Oswald:wght@400;700&display=swap">
<style>
  :root {
    --page: #1c1712;
    --gilt-dark: #7a4f14;
    --gilt-mid: #c1913a;
    --gilt-light: #ecc86e;
    --plank-light: #e4e1da;
    --plank-mid: #cfcac0;
    --plank-dark: #a8a297;
    --ink: #4a3428;
    --tagline: #f7f4ee;
    --tagline-edge: rgba(60, 45, 35, 0.45);
  }
  * { margin: 0; padding: 0; box-sizing: border-box; }
  html, body {
    width: 778px; height: 1200px; overflow: hidden;
    background: var(--page);
  }
  .cover {
    position: relative;
    width: 778px; height: 1200px;
  }
  .gilded-frame {
    position: absolute; inset: 0;
    background:
      linear-gradient(135deg, var(--gilt-light) 0%, var(--gilt-mid) 22%, var(--gilt-dark) 45%, var(--gilt-mid) 70%, var(--gilt-light) 100%);
  }
  .frame-bead {
    position: absolute;
    left: 100px; top: 100px; right: 100px; bottom: 119px;
    border: 8px solid var(--gilt-light);
    box-shadow: 0 0 0 4px var(--gilt-dark), inset 0 0 0 4px var(--gilt-dark);
  }
  .canvas-panel {
    position: absolute;
    left: 118px; top: 118px;
    width: 542px; height: 945px;
    background:
      linear-gradient(90deg, var(--plank-mid) 0%, var(--plank-light) 18%, var(--plank-mid) 35%, var(--plank-light) 55%, var(--plank-dark) 62%, var(--plank-light) 78%, var(--plank-mid) 100%);
    overflow: hidden;
  }
  .lettering {
    position: absolute; inset: 0;
    width: 542px; height: 945px;
  }
  .author-name, .title {
    font-family: "Oswald", sans-serif;
    font-weight: 700;
  }
  .author-name { fill: url(#author-fill); }
  .title { fill: url(#portrait-fill); }
  .tagline {
    font-family: "Oswald", sans-serif;
    font-weight: 400;
    font-size: 27px;
    fill: var(--tagline);
    stroke: var(--tagline-edge);
    stroke-width: 0.8px;
    paint-order: stroke;
  }
</style>
</head>
<body>
<main class="cover">
  <div class="gilded-frame" role="img" aria-label="Ornate carved gilt picture frame"></div>
  <div class="frame-bead"></div>
  <section class="canvas-panel">
    <svg class="lettering" viewBox="0 0 542 945" xmlns="http://www.w3.org/2000/svg">
      <defs>
        <linearGradient id="author-fill" x1="0" x2="1" y1="0" y2="0">
          <stop offset="0" stop-color="#3a2a21"/>
          <stop offset="0.5" stop-color="#6a4a38"/>
          <stop offset="1" stop-color="#3a2a21"/>
        </linearGradient>
        <radialGradient id="portrait-fill" gradientUnits="userSpaceOnUse" cx="300" cy="540" r="300">
          <stop offset="0" stop-color="#e8c2ac"/>
          <stop offset="0.25" stop-color="#d39a86"/>
          <stop offset="0.4" stop-color="#b8332c"/>
          <stop offset="0.6" stop-color="#6b4a3a"/>
          <stop offset="1" stop-color="#1f1712"/>
        </radialGradient>
      </defs>
      <text class="author-name" x="6" y="258" font-size="165" textLength="530" lengthAdjust="spacingAndGlyphs">MARLENE</text>
      <text class="tagline" x="271" y="338" text-anchor="middle" textLength="470" lengthAdjust="spacingAndGlyphs">WHY, IN A HOUSE FULL OF PORTRAITS,</text>
      <g role="img" aria-label="Oil portrait of a young woman glimpsed through the title letters">
        <text class="title" x="4" y="621" font-size="290" textLength="534" lengthAdjust="spacingAndGlyphs">HOLLOWED</text>
      </g>
      <text class="tagline" x="271" y="703" text-anchor="middle" textLength="400" lengthAdjust="spacingAndGlyphs">DOES ONE STAND UNFINISHED?</text>
      <text class="author-name" x="6" y="880" font-size="165" textLength="530" lengthAdjust="spacingAndGlyphs">OSGOOD</text>
    </svg>
  </section>
</main>
</body>
</html>
```